I am looking for a flyer design for my upcoming symposium. Here are the details for the flyer and pictures of speakers are attached.

Name of Symposium: Lattice and Pathway Biosciences Symposium, Sponsored by the Corvale Chromatin Institute and the Department of Bioengineering
Date: January 8, 2018
Location: Havergill Auditorium, Tarnby Center for Applied Discovery, 2175 Orchard Terrace Ave, Philadelphia, PA 19127

Reception to follow after the symposium.

Also, please add - Register and upload abstracts for the symposium at www.qzvmrk.com. Registration and abstract submission closes on January 4, 2018.

Keynote Speaker:
Marthe Quillon, Ph.D.
NTVO Director General; Professor, Lyceum of Norvane; Director, Genetics and Developmental Biology at Institut Bramoux
Lyceum of Norvane, NTVO, Institut Bramoux
"Title of talk TBA."

Speakers:
Lena Drewcott, Ph.D.
Assistant Professor of Cell and Developmental Biology
Halvering State University, HMCS
"Title of talk TBA."

Paul Marden, Ph.D.
Assistant Professor of Genetics
"Title of talk TBA."

Ilse Varga, Ph.D.
Professor, Ostrander University
Otto Wenzlau Center for Molecular Medicine
"Title of talk TBA."

Jun Hao, Ph.D.
Professor of Cellular and Molecular Medicine
Coastal Meridian University
"Title of talk TBA."

Wei Lun, Ph.D.
Associate Professor of Pediatrics
The Youth Medical Pavilion of Philadelphia
"Spatial genome re-organization between fetal and adult hematopoietic stem cells."

Mei Zhou, Ph.D.
Professor, Department of Genetics
Ellsworth Medical School
"Title of talk TBA."

```html
<!DOCTYPE html>
<html lang="en">
<head>
<meta charset="utf-8">
<title>Lattice and Pathway Biosciences Symposium</title>
<link rel="stylesheet" href="https://fonts.googleapis.com/css2?family=Bebas+Neue&family=Montserrat:wght@800;900&family=Quicksand:wght@500;600;700&display=swap">
<style>
:root{
  --teal:#16858a;
  --teal-dark:#0f7479;
  --backdrop:#3b3b3d;
  --paper:#ffffff;
  --ink-light:#ffffff;
}
*{margin:0;padding:0;box-sizing:border-box}
html,body{width:849px;height:1200px;overflow:hidden;background:var(--backdrop)}
body{position:relative;font-family:"Quicksand",sans-serif;color:var(--ink-light)}
.flyer{position:absolute;left:66px;top:92px;width:717px;height:1016px;background:var(--paper)}
.title-band{position:absolute;left:15px;top:24px;width:687px;height:191px;background:var(--teal);border-radius:10px 10px 0 0;display:flex;align-items:center;justify-content:center}
.title-band h1{font-family:"Bebas Neue",sans-serif;font-weight:400;font-size:184px;line-height:1;letter-spacing:4px;margin-top:14px;color:var(--ink-light)}
.subtitle{position:absolute;left:0;top:226px;width:717px;text-align:center;color:var(--teal);font-weight:700;font-size:18.5px;line-height:23px}
.panel{position:absolute;left:15px;top:282px;width:687px;height:649px;background:var(--teal);border-radius:0 0 12px 12px}
.speaker{position:absolute;display:flex;gap:10px;width:320px}
.photo{flex:none;width:89px;height:102px;border:2px solid #fff;border-radius:5px;background:linear-gradient(160deg,#b9a48f,#6c5a4c)}
.info{padding-top:6px}
.role{font-size:10.5px;font-weight:600;margin-bottom:2px}
.name{font-size:17.5px;font-weight:700;line-height:20px}
.detail{font-size:10.3px;font-weight:600;line-height:13.4px}
.date{position:absolute;left:396px;top:30px;font-family:"Montserrat",sans-serif;font-weight:900;color:#fff;line-height:1}
.date .month{position:absolute;left:0;top:6px;font-size:26px;letter-spacing:0.5px}
.date .year{position:absolute;left:0;top:36px;font-size:56px;letter-spacing:-1px}
.date .day{position:absolute;left:164px;top:-8px;font-size:112px;letter-spacing:-2px}
.register{position:absolute;left:14px;top:481px;width:659px;height:149px;background:#fff;border-radius:12px}
.register .cta{position:absolute;left:0;top:10px;width:466px;text-align:center;color:var(--teal);font-weight:700}
.cta .line{font-size:17.5px;line-height:22px}
.cta .url{font-family:"Montserrat",sans-serif;font-weight:800;font-size:41px;line-height:44px;letter-spacing:1px}
.cta .deadline{font-family:"Montserrat",sans-serif;font-weight:800;font-size:43px;line-height:48px;letter-spacing:0.5px}
.divider{position:absolute;left:465px;top:12px;width:1px;height:125px;background:#d6d6d6}
.sponsor{position:absolute;left:482px;display:flex;align-items:center;gap:8px;color:var(--teal-dark);font-weight:700;font-size:15px;line-height:17px}
.sponsor .mark{width:26px;height:26px;border-radius:50%;background:var(--teal)}
.venue{position:absolute;left:0;top:945px;width:717px;height:71px;background:var(--teal);text-align:center;font-weight:700;font-size:19px;line-height:23px;padding-top:12px}
</style>
</head>
<body>
<main class="flyer">
  <header class="title-band"><h1>SYMPOSIUM</h1></header>
  <p class="subtitle">Lattice and Pathway Biosciences Symposium, Sponsored by the<br>Corvale Chromatin Institute and the Department of Bioengineering</p>

  <section class="panel">
    <div class="date"><span class="month">JANUARY</span><span class="year">201</span><span class="day">8</span></div>

    <article class="speaker" style="left:23px;top:24px;width:360px">
      <div class="photo" role="img" aria-label="Portrait photo of Marthe Quillon"></div>
      <div class="info">
        <p class="role">Keynote Speaker:</p>
        <p class="name">Marthe Quillon, Ph.D.</p>
        <p class="detail">NTVO Director General; Professor, Lyceum of Norvane:<br>Director, Genetics and Developmental Biology at Ins.<br>Lyceum of Norvane, NTVO, Institut Bramoux<br>"Title of talk TBA."</p>
      </div>
    </article>

    <article class="speaker" style="left:23px;top:135px">
      <div class="photo" role="img" aria-label="Portrait photo of Lena Drewcott"></div>
      <div class="info">
        <p class="role">Speakers:</p>
        <p class="name">Lena Drewcott, Ph.D.</p>
        <p class="detail">Assistant Professor of Cell and<br>Developmental Biology<br>Halvering State University, HMCS<br>"Title of talk TBA."</p>
      </div>
    </article>

    <article class="speaker" style="left:23px;top:247px">
      <div class="photo" role="img" aria-label="Portrait photo of Jun Hao"></div>
      <div class="info">
        <p class="name">Jun Hao, Ph.D.</p>
        <p class="detail">Professor of Cellular and Molecular<br>Medicine<br>Coastal Meridian University<br>"Title of talk TBA."</p>
      </div>
    </article>

    <article class="speaker" style="left:23px;top:359px;width:340px">
      <div class="photo" role="img" aria-label="Portrait photo of Wei Lun"></div>
      <div class="info">
        <p class="name" style="margin-top:8px">Wei Lun, Ph.D.</p>
        <p class="detail">Associate Professor of Pediatrics<br>The Youth Medical Pavilion of Philadelphia<br>"Spatial genome re-organization between<br>fetal and adult hematopoietic stem cells."</p>
      </div>
    </article>

    <article class="speaker" style="left:379px;top:135px">
      <div class="photo" role="img" aria-label="Portrait photo of Paul Marden"></div>
      <div class="info">
        <p class="name" style="margin-top:14px">Paul Marden, Ph.D.</p>
        <p class="detail">Assistant Professor of Genetics<br>Halvering State University, HMCS<br>"Title of talk TBA."</p>
      </div>
    </article>

    <article class="speaker" style="left:379px;top:247px">
      <div class="photo" role="img" aria-label="Portrait photo of Ilse Varga"></div>
      <div class="info">
        <p class="name">Ilse Varga, Ph.D.</p>
        <p class="detail">Professor, Ostrander University<br>Otto Wenzlau Center for Molecular<br>Medicine<br>"Title of talk TBA."</p>
      </div>
    </article>

    <article class="speaker" style="left:379px;top:359px">
      <div class="photo" role="img" aria-label="Portrait photo of Mei Zhou"></div>
      <div class="info">
        <p class="name" style="margin-top:14px">Mei Zhou, Ph.D.</p>
        <p class="detail">Professor, Department of Genetics<br>Ellsworth Medical School<br>"Title of talk TBA."</p>
      </div>
    </article>

    <aside class="register">
      <div class="cta">
        <p class="line">Register and upload abstracts for the symposium at</p>
        <p class="url">WWW.QZVMRK.COM</p>
        <p class="line">Registration and abstract submission closes on</p>
        <p class="deadline">JANUARY 4, 2018</p>
      </div>
      <div class="divider"></div>
      <div class="sponsor" style="top:22px"><span class="mark"></span><span>Corvale Chromatin<br>Institute</span></div>
      <div class="sponsor" style="top:88px"><span class="mark"></span><span>Brackwell<br>Engineering</span></div>
    </aside>
  </section>

  <footer class="venue">Havergill Auditorium, Tarnby Center for Applied Discovery,<br>2175 Orchard Terrace Ave, Philadelphia, PA 19127</footer>
</main>
</body>
</html>
```